plain circle Bootstrap Website Design (Gaming Themed)

I need a website designed using plain circle Bootstrap for a Rewards website. We'd like to see a gaming based design as the site will cater mostly to gamers.
This is a rewards site similar to sites like LootPenny
I only need the HTML/CSS design.
I need these pages:
1. Homepage for non-logged in users which will also have a sign up form
2. Homepage for logged in users
3. Profile Page
4. Rewards page which will display items that the user can redeem
a) A drop-down to sort by item category
5. Rewards page item details which will display a single item's details
6. About, FAQ, Terms Of Service Pages
Target Market(s)
13 to 30 year old gamers
Mostly males
Industry/Entity Type
It Service
Look and feel

```html
<!DOCTYPE html>
<html lang="en">
<head>
<meta charset="utf-8">
<title>Pinecrest Gaming – Rewards</title>
<link rel="stylesheet" href="https://fonts.googleapis.com/css2?family=Roboto+Condensed:ital,wght@0,400;0,700;1,400&family=PT+Sans:ital,wght@0,400;0,700;1,400&family=Tinos&display=swap">
<style>
:root{
  --brand-red:#e0301e;
  --brand-red-dark:#b8200f;
  --ink:#333333;
  --mid-gray:#7a7a7a;
  --panel-dark:#333333;
  --footer-dark:#262626;
  --base-dark:#1e1e1e;
  --muted:#9a9a9a;
  --white:#ffffff;
}
*{margin:0;padding:0;box-sizing:border-box}
html,body{width:1200px;height:1029px;overflow:hidden;background:var(--base-dark)}
body{position:relative;font-family:"PT Sans",sans-serif}
.abs{position:absolute}

/* header */
.site-header{position:absolute;left:0;top:0;width:1200px;height:75px;background:var(--brand-red)}
.brand{position:absolute;left:180px;top:19px;color:var(--white);font-family:"Roboto Condensed",sans-serif;font-weight:700;font-size:30px;line-height:36px;letter-spacing:-.5px}
.main-nav a{position:absolute;top:31px;color:var(--white);font-family:"Roboto Condensed",sans-serif;font-size:12px;text-decoration:none}
.nav-signup{position:absolute;left:918px;top:24px;width:99px;height:26px;background:var(--brand-red-dark);border-radius:3px;color:var(--white);font-family:"Roboto Condensed",sans-serif;font-size:12px;text-align:center;line-height:26px}

/* hero */
.hero{position:absolute;left:0;top:75px;width:1200px;height:492px}
.hero-photo{position:absolute;inset:0;background:linear-gradient(160deg,#f4f6f8 0%,#e6ecf2 30%,#8fb3d9 55%,#5e8fc7 70%,#dfe6ee 88%,#c9d3de 100%)}
.hero-arrow{position:absolute;top:222px;width:34px;height:34px}
.hero-copy{position:absolute;left:180px;width:490px;text-align:center;font-family:"Roboto Condensed",sans-serif;font-weight:400}
.hero-title{top:157px;color:var(--brand-red);font-size:39px;line-height:46px;font-weight:700}
.hero-sub{top:213px;color:var(--ink);font-size:22px;line-height:28px}
.hero-rule{position:absolute;left:207px;width:453px;height:3px;border-top:1px solid var(--brand-red);border-bottom:1px solid #3a4a8a}
.hero-earned{top:287px;font-family:"Tinos",serif;color:#222;font-size:23px;line-height:28px}
.hero-total{top:320px;color:var(--brand-red);font-size:38px;line-height:46px;font-weight:700}

.signup-card{position:absolute;left:735px;top:90px;width:285px;height:299px;background:var(--white)}
.signup-title{position:absolute;left:0;top:17px;width:275px;text-align:center;color:var(--brand-red);font-family:"Roboto Condensed",sans-serif;font-weight:400;font-size:25px}
.signup-sub{position:absolute;left:0;top:52px;width:285px;text-align:center;color:var(--mid-gray);font-family:"Roboto Condensed",sans-serif;font-size:14px}
.signup-rule{position:absolute;left:27px;top:81px;width:232px;border-top:1px solid #cfcfcf}
.field{position:absolute;left:27px;width:232px;height:26px;border:1px solid #c8c8c8;padding-left:13px;font-size:9px;line-height:24px;color:var(--mid-gray)}
.signup-code{position:absolute;left:0;top:217px;width:285px;text-align:center;font-size:9px;color:var(--mid-gray)}
.signup-button{position:absolute;left:64px;top:236px;width:161px;height:33px;background:linear-gradient(#5d5d60,#48484b);border-radius:2px;color:var(--white);text-align:center;line-height:33px;font-family:"Roboto Condensed",sans-serif;font-size:15px}

/* how it works */
.how{position:absolute;left:0;top:567px;width:1200px;height:238px;background:var(--panel-dark)}
.video-frame{position:absolute;left:185px;top:47px;width:249px;height:148px}
.video-still{position:absolute;left:0;top:0;width:249px;height:135px;background:radial-gradient(circle at 55% 45%,#6a6a72,#1c1c22 70%)}
.video-bar{position:absolute;left:0;top:135px;width:249px;height:13px;background:#e8e8e8;font-size:6px;color:#222;line-height:13px}
.how-title{position:absolute;left:471px;top:47px;color:var(--white);font-family:"Roboto Condensed",sans-serif;font-weight:400;font-size:21px}
.how-text{position:absolute;left:471px;top:91px;width:540px;color:#b8b8b8;font-style:italic;font-size:9.6px;line-height:17px}

/* footer */
.site-footer{position:absolute;left:0;top:805px;width:1200px;height:175px;background:var(--footer-dark)}
.footer-col{position:absolute;top:23px}
.footer-col h4{color:var(--white);font-size:12px;font-weight:700;margin-bottom:6px}
.footer-col li{list-style:none;color:var(--muted);font-size:8px;line-height:17px;text-transform:uppercase}
.base-bar{position:absolute;left:0;top:980px;width:1200px;height:49px;background:var(--base-dark)}
.copyright{position:absolute;left:188px;top:19px;color:var(--muted);font-size:8.5px}
.follow{position:absolute;left:846px;top:19px;color:var(--muted);font-size:8.5px}
.social{position:absolute;top:11px;width:26px;height:26px;border-radius:50%}
</style>
</head>
<body>

<header class="site-header">
  <div class="brand">Pinecrest Gaming</div>
  <nav class="main-nav">
    <a style="left:628px">HOME</a>
    <a style="left:726px">ABOUT US</a>
    <a style="left:844px">REWARDS</a>
  </nav>
  <div class="nav-signup">SIGNUP NOW</div>
</header>

<section class="hero">
  <div class="hero-photo" role="img" aria-label="Photo of a skier carving down a snowy mountain slope under a blue sky"></div>
  <svg class="hero-arrow" style="left:82px" viewBox="0 0 34 34"><circle cx="17" cy="17" r="15.5" fill="none" stroke="#fff" stroke-width="2"/><path d="M20 9 11 17l9 8z" fill="#fff"/></svg>
  <svg class="hero-arrow" style="left:1085px" viewBox="0 0 34 34"><circle cx="17" cy="17" r="15.5" fill="none" stroke="#fff" stroke-width="2"/><path d="M14 9l9 8-9 8z" fill="#fff"/></svg>

  <h1 class="hero-copy hero-title">WATCH THE REWARDS ROLL IN</h1>
  <p class="hero-copy hero-sub">START EARNING FREE GIFT CARDS TODAY!</p>
  <div class="hero-rule" style="top:270px"></div>
  <p class="hero-copy hero-earned">MEMBERS HAVE EARNED</p>
  <p class="hero-copy hero-total">$47,540,452 IN REWARDS</p>
  <div class="hero-rule" style="top:377px"></div>

  <form class="signup-card">
    <h2 class="signup-title">Sign up For News</h2>
    <p class="signup-sub">or sign up with your email below</p>
    <div class="signup-rule"></div>
    <div class="field" style="top:100px">EMAIL ADDRESS :</div>
    <div class="field" style="top:137px">PASSWORD :</div>
    <div class="field" style="top:174px">CONFIRM PASSWORD :</div>
    <p class="signup-code">I HAVE A SIGN UP CODE (OPTIONAL)</p>
    <div class="signup-button">GET STARTED</div>
  </form>
</section>

<section class="how">
  <div class="video-frame">
    <div class="video-still" role="img" aria-label="Video still of two boxers trading punches in a ring"></div>
    <svg class="abs" style="left:98px;top:40px" width="54" height="54" viewBox="0 0 54 54"><circle cx="27" cy="27" r="26" fill="rgba(255,255,255,.25)"/><path d="M21 16l17 11-17 11z" fill="rgba(255,255,255,.7)"/></svg>
    <div class="video-bar">
      <svg class="abs" style="left:5px;top:3px" width="6" height="7"><path d="M0 0l6 3.5L0 7z" fill="#222"/></svg>
      <span class="abs" style="left:20px">00:00</span>
      <span class="abs" style="left:42px;top:5px;width:134px;height:3px;background:#aaa"></span>
      <span class="abs" style="left:182px">00:00</span>
    </div>
  </div>
  <h2 class="how-title">HOW DOES IT WORK?</h2>
  <p class="how-text">It is a long established fact that a reader will be distracted by the readable content of a page when looking at its layout. The point of using Lorem Ipsum is that it has a more-or-less normal distribution of letters, as opposed to using 'Content here, content here', making it look like readable English. Many desktop publishing packages and web page editors now use Lorem Ipsum as their default model text, and a search for 'lorem ipsum' will uncover many web sites still in their infancy. Various versions have evolved over the years, sometimes by accident, sometimes on purpose</p>
</section>

<footer class="site-footer">
  <div class="footer-col" style="left:192px"><h4>WELCOME</h4><ul><li>Home</li><li>About Us</li><li>Blog</li><li>Newsletter</li><li>Toolbars &amp; Plugins</li></ul></div>
  <div class="footer-col" style="left:355px"><h4>WAYS TO EARN</h4><ul><li>Search</li><li>Answer</li><li>Discover</li></ul></div>
  <div class="footer-col" style="left:526px"><h4>REWARDS</h4><ul><li>Rewards Store</li><li>Lootstakes</li></ul></div>
  <div class="footer-col" style="left:689px"><h4>INFORMATION</h4><ul><li>Do's and Dont's</li><li>Help Center</li><li>How It Works</li><li>Winning Tips</li><li>In The Press</li><li>Sitemap</li></ul></div>
  <div class="footer-col" style="left:869px"><h4>SUPPORT</h4><ul><li>Contact Us</li><li>Business Development</li><li>Advertise With Us</li><li>Sweepstakes Rules</li><li>Privacy Policy</li><li>Terms Of Use</li><li>Press Inquiries</li></ul></div>
</footer>

<div class="base-bar">
  <p class="copyright">COPYRIGHT © 2013. PINECREST GAMING. ALL RIGHTS RESERVED.</p>
  <p class="follow">FOLLOW US :</p>
  <span class="social" style="left:905px;background:#555"></span>
  <span class="social" style="left:934px;background:#555"></span>
  <span class="social" style="left:962px;background:#555"></span>
  <span class="social" style="left:991px;background:var(--brand-red)"></span>
</div>

</body>
</html>
```